VORDA HOMES PELAB MARKETING FLYER

THE FLYER CAN BE FRONT TO BACK OR 2 PAGES IF NEEDED.

need to create a flyer with the following information:

Tallyworth Inc. is a CRM (Customer Relationship Management System) that provides leads to agents and a system to communicate and track your leads. Initial training and set up will be provided

Commission splits for leads are as follows: (maybe we can create a chart or box for items 1-3)

1. Cold leads 40% Vorda - 60% Agent - Worked by Agent in the platform, agent shows property, writes contract, handles all negotiations and any necessary addendums, attends home inspection and settlement.

2. Warm leads 50% Vorda - 50% Co-agent - Contacted by ISA, agent shows property, writes contract, handles all negotiations and any necessary addendums, attends home inspection and settlement.

3 Hot leads 70% Vorda - 30% Co-agent - Prequalified by Vorda Homes and ready to look at property, Vorda writes contract and secures broker agency relationship agreements, co-agent shows property, , handles all negotiations (with support from VORDA if necessary), execute any necessary addendums, attend home inspection and settlement.

Preferred vendors such as Lender, Title, Insurance, Home Inspector, etc. are to be used for any transactions related to PELB per Vorda Homes.

Agents will receive 10 leads for free to start once Fresh Broker Launchpad is complete. Warm leads will be available to purchase for $15 each beyond the first 10. Every 5 deals closed, agent commission will increase by 10% annually!!

Rules and restrictions apply.

3. In addition to Quillset, a transaction coordinator included.

4. Free PELB Support and training included

5. Free personal CRM website included

Industry/Entity Type

Real Estate

Colors
3176b5
85abd2
ecf5f6

Requirements
Must have
• everything in the description above

```html
<!DOCTYPE html>
<html lang="en">
<head>
<meta charset="utf-8">
<title>Vorda Homes PELB Agent Flyer</title>
<link rel="stylesheet" href="https://fonts.googleapis.com/css2?family=Montserrat:wght@400;500;600&family=Oswald:wght@400;500&display=swap">
<style>
  :root {
    --brand-blue: #3176b5;
    --soft-blue: #85abd2;
    --mist: #ecf5f6;
    --navy: #233a7a;
    --charcoal: #4a4d52;
    --teal: #1ea3a5;
    --cold: #2ea7cf;
    --warm: #ecc52a;
    --hot: #ee5a24;
    --ink: #1f2226;
    --backdrop: #a9a9a9;
    --white: #ffffff;
  }
  * { box-sizing: border-box; margin: 0; padding: 0; }
  html, body { width: 1200px; height: 2400px; overflow: hidden; }
  body { background: var(--backdrop); font-family: 'Montserrat', sans-serif; color: var(--ink); position: relative; }

  .flyer { position: absolute; left: 50px; top: 489px; width: 1100px; height: 1422px; background: var(--white); overflow: hidden; box-shadow: 0 10px 30px rgba(0,0,0,.25); }

  .masthead { position: absolute; left: 0; top: 0; width: 100%; height: 229px; }
  .masthead .divider { position: absolute; top: 35px; width: 2px; height: 167px; background: var(--ink); }
  .brand { position: absolute; top: 0; height: 229px; display: flex; align-items: center; justify-content: center; gap: 10px; font-weight: 600; }
  .brand-pelb { left: 150px; width: 250px; font-size: 58px; color: var(--charcoal); letter-spacing: 1px; }
  .brand-pelb .mark { width: 22px; height: 22px; background: var(--teal); }
  .brand-vorda { left: 420px; width: 285px; font-size: 40px; color: var(--navy); letter-spacing: 2px; }
  .brand-harbor { left: 725px; width: 280px; font-size: 19px; color: var(--brand-blue); }
  .brand-harbor .mark { width: 16px; height: 16px; border-radius: 50%; background: var(--brand-blue); }

  .hero { position: absolute; left: 0; top: 229px; width: 100%; height: 462px; background: linear-gradient(100deg, #c9cbcf 0%, #e6e2de 30%, #d9a88f 48%, #c98c77 58%, #eae8e6 72%, #3a4050 88%, #f4f5f7 100%); }

  .intro { position: absolute; left: 35px; top: 430px; width: 331px; height: 354px; background: var(--brand-blue); color: var(--white); padding: 36px 22px 0; text-align: center; z-index: 3; }
  .intro-lead { font-size: 18px; font-weight: 600; line-height: 1.2; padding: 0 12px 14px; }
  .intro-list { list-style: none; }
  .intro-list li { border-top: 1.5px solid rgba(255,255,255,.85); font-size: 16.5px; font-weight: 600; line-height: 1.3; padding: 9px 0; }

  .split-band { position: absolute; left: 0; top: 691px; width: 100%; height: 80px; }
  .split-band svg { position: absolute; inset: 0; }
  .split-band h2 { position: absolute; left: 465px; right: 0; top: 0; height: 80px; display: flex; align-items: center; justify-content: center; font-size: 21px; font-weight: 600; color: var(--white); letter-spacing: .3px; }

  .lead-card { position: absolute; top: 803px; width: 322px; height: 287px; color: var(--white); text-align: center; box-shadow: 0 12px 10px -8px rgba(0,0,0,.35); }
  .lead-cold { left: 35px; background: var(--cold); }
  .lead-warm { left: 394px; background: var(--warm); color: var(--ink); }
  .lead-hot { left: 753px; background: var(--hot); }
  .lead-warm .lead-title { color: var(--white); }
  .lead-title { font-family: 'Oswald', sans-serif; font-weight: 500; font-size: 28px; padding-top: 12px; height: 62px; }
  .lead-ribbon { position: absolute; left: -14px; top: 62px; width: 350px; height: 36px; }
  .lead-ribbon svg { position: absolute; inset: 0; }
  .lead-ribbon span { position: relative; display: block; line-height: 36px; font-size: 17px; font-weight: 600; color: var(--white); letter-spacing: .5px; }
  .lead-body { position: absolute; left: 18px; right: 18px; top: 130px; font-size: 13.6px; line-height: 1.27; }
  .lead-hot .lead-body { top: 112px; }

  .fine-print { position: absolute; left: 33px; top: 1131px; width: 590px; font-size: 18.5px; line-height: 1.18; }
  .fine-print p { margin-bottom: 22px; }
  .fine-print .rules { margin-bottom: 0; }

  .perks { position: absolute; left: 687px; top: 1162px; width: 400px; list-style: none; font-size: 18.5px; line-height: 1.18; }
  .perks li { display: flex; gap: 8px; margin-bottom: 21px; }
  .perks svg { flex: 0 0 22px; margin-top: 1px; }

  .contact-bar { position: absolute; left: 0; top: 1358px; width: 100%; height: 47px; }
  .contact-bar svg { position: absolute; inset: 0; }
  .contact-bar span { position: absolute; top: 0; line-height: 47px; font-size: 18.5px; color: var(--white); }
</style>
</head>
<body>
<main class="flyer">
  <header class="masthead">
    <div class="brand brand-pelb"><span class="mark"></span>PELB</div>
    <span class="divider" style="left:411px"></span>
    <div class="brand brand-vorda">VORDA HOMES</div>
    <span class="divider" style="left:713px"></span>
    <div class="brand brand-harbor"><span class="mark"></span>Harborline Realty Group</div>
  </header>

  <div class="hero" role="img" aria-label="Photo of two business people shaking hands beside a small model house"></div>

  <section class="intro">
    <p class="intro-lead">Tallyworth Inc. is a CRM (Customer Relationship Management System) that provides</p>
    <ul class="intro-list">
      <li>LEADS TO AGENTS</li>
      <li>A SYSTEM TO COMMUNICATE</li>
      <li>TRACK YOUR LEADS<br>INITIAL TRAINING</li>
      <li>SET UP WILL BE PROVIDED</li>
    </ul>
  </section>

  <div class="split-band">
    <svg width="1100" height="80" viewBox="0 0 1100 80">
      <rect x="0" y="0" width="1100" height="14" fill="#b9cde6"/>
      <polygon points="465,0 1100,0 1100,80 492,80 475,46 465,14" fill="var(--soft-blue)"/>
      <polygon points="465,14 475,46 492,80 485,80 468,46 458,14" fill="#b9cde6"/>
    </svg>
    <h2>COMMISSION SPLITS FOR LEADS ARE AS FOLLOWS:</h2>
  </div>

  <article class="lead-card lead-cold">
    <h3 class="lead-title">COLD LEADS</h3>
    <div class="lead-ribbon">
      <svg width="350" height="36" viewBox="0 0 350 36"><polygon points="0,0 350,0 338,18 350,36 0,36 12,18" fill="var(--brand-blue)"/></svg>
      <span>40% VORDA - 60% CO-AGENT</span>
    </div>
    <p class="lead-body">Worked by Agent in the platform, agent shows property, writes contract, handles all negotiations and any necessary addendums, attends home inspection and settlement.</p>
  </article>

  <article class="lead-card lead-warm">
    <h3 class="lead-title">WARM LEADS</h3>
    <div class="lead-ribbon">
      <svg width="350" height="36" viewBox="0 0 350 36"><polygon points="0,0 350,0 338,18 350,36 0,36 12,18" fill="var(--brand-blue)"/></svg>
      <span>50% VORDA - 50% CO-AGENT</span>
    </div>
    <p class="lead-body">Contacted by ISA, agent shows property, writes contract, handles all negotiations and any necessary addendums, attends home inspection and settlement.</p>
  </article>

  <article class="lead-card lead-hot">
    <h3 class="lead-title">HOT LEADS</h3>
    <div class="lead-ribbon">
      <svg width="350" height="36" viewBox="0 0 350 36"><polygon points="0,0 350,0 338,18 350,36 0,36 12,18" fill="var(--brand-blue)"/></svg>
      <span>70% VORDA - 30% CO-AGENT</span>
    </div>
    <p class="lead-body">Prequalified by Vorda Homes and ready to look at property, Vorda writes contract and secures broker agency relationship agreements, co-agent shows property, , handles all negotiations (with support from VORDA if necessary), execute any necessary addendums, attend home inspection and settlement.</p>
  </article>

  <section class="fine-print">
    <p>Preferred vendors such as Lender, Title, Insurance, Home Inspector, etc. are to be used for any transactions related to PELB per Vorda Homes.</p>
    <p>Agents will receive 10 leads for free to start once Fresh Broker Launchpad is complete.&nbsp; Warm leads will be available to purchase for $15 each beyond the first 10.&nbsp; Every 5 deals closed, agent commission will increase by 10% annually!!</p>
    <p class="rules">* Rules and restrictions apply.</p>
  </section>

  <ul class="perks">
    <li><svg width="22" height="22" viewBox="0 0 22 22"><circle cx="11" cy="11" r="10" fill="var(--brand-blue)"/><path d="M6 11.5l3.3 3.2L16 8" fill="none" stroke="#fff" stroke-width="2.2"/></svg><span>In addition to Quillset, a transaction coordinator included.</span></li>
    <li><svg width="22" height="22" viewBox="0 0 22 22"><circle cx="11" cy="11" r="10" fill="var(--brand-blue)"/><path d="M6 11.5l3.3 3.2L16 8" fill="none" stroke="#fff" stroke-width="2.2"/></svg><span>Free PELB Support and training included</span></li>
    <li><svg width="22" height="22" viewBox="0 0 22 22"><circle cx="11" cy="11" r="10" fill="var(--brand-blue)"/><path d="M6 11.5l3.3 3.2L16 8" fill="none" stroke="#fff" stroke-width="2.2"/></svg><span>Free personal CRM website included</span></li>
  </ul>

  <footer class="contact-bar">
    <svg width="1100" height="47" viewBox="0 0 1100 47">
      <rect x="0" y="0" width="1100" height="47" fill="var(--soft-blue)"/>
      <polygon points="0,0 383,0 402,47 0,47" fill="var(--brand-blue)"/>
    </svg>
    <span style="left:34px">812 Alder Crest Lane, Suite 410</span>
    <span style="left:440px">555-014-2870</span>
    <span style="left:637px">info@vordahomes.net</span>
    <span style="left:873px">www.vordahomes.com</span>
  </footer>
</main>
</body>
</html>
```